Coffee bag stamp design for new coffee brand

Stamp design that will be used like a label on a coffee package.
It must be a vector that can be produced as a stamp. Coffee bag is from brown craft paper. I upload image of this bag. Size of design is 80mm x 140mm.
I also uploaded two pictures for inspiration, but I will also appreciate new ideas.

Target Market(s)

Coffee lovers, who love to try new coffee. Also hipsters.

Colors

Designer to choose only greyscale colors for use in the design.

Requirements
Must have
• Some information about coffee must have:
Name: BRAZIL (the biggest font in that design)
Region: Santos
Altitude: 60 – 1200 m.n.m.
Variety: Arabica
Processing: unwashed

```html
<!DOCTYPE html>
<html lang="en">
<head>
<meta charset="utf-8">
<title>Brazil Santos – Coffee Stamp</title>
<link rel="stylesheet" href="https://fonts.googleapis.com/css2?family=Bebas+Neue&display=swap">
<style>
  :root {
    --paper: #fefefe;
    --ink: #000000;
  }
  html, body {
    margin: 0;
    padding: 0;
    width: 1200px;
    height: 848px;
    overflow: hidden;
    background: var(--paper);
  }
  .stamp {
    display: block;
    width: 1200px;
    height: 848px;
  }
  .stamp text {
    font-family: "Bebas Neue", "Oswald", sans-serif;
    fill: var(--ink);
  }
  .frame-outer { fill: none; stroke: var(--ink); stroke-width: 3.6; }
  .rule { stroke: var(--ink); stroke-width: 2; }
  .name-main { font-size: 48px; }
  .name-region { font-size: 29px; }
  .variety { font-size: 18px; }
  .spec { font-size: 13px; }
  .steam-area { fill: var(--ink); }
  .bean { fill: var(--ink); }
  .bean-crease { fill: none; stroke: var(--paper); stroke-width: 1.2; stroke-linecap: round; }
</style>
</head>
<body>
<svg class="stamp" viewBox="0 0 1200 848" xmlns="http://www.w3.org/2000/svg">
  <!-- frame -->
  <rect class="frame-outer" x="509.8" y="257.8" width="159.4" height="316.4"/>
  <line class="rule" x1="511" y1="268.5" x2="668" y2="268.5"/>
  <line class="rule" x1="511" y1="562.5" x2="668" y2="562.5"/>

  <!-- steam symbol area -->
  <rect class="steam-area" x="581" y="288" width="20" height="35" rx="6"
        role="img" aria-label="Rising steam symbol"/>

  <!-- origin name -->
  <text class="name-main" x="526" y="371" textLength="126" lengthAdjust="spacing">BRAZIL</text>
  <text class="name-region" x="528" y="400" textLength="123" lengthAdjust="spacing">SANTOS</text>

  <line class="rule" x1="511" y1="418" x2="668" y2="418"/>

  <!-- variety -->
  <text class="variety" x="529" y="442" textLength="121" lengthAdjust="spacing">ARABICA COFFEE</text>

  <line class="rule" x1="511" y1="454" x2="668" y2="454"/>
  <line class="rule" x1="589" y1="454" x2="589" y2="500"/>
  <line class="rule" x1="511" y1="500" x2="668" y2="500"/>

  <!-- altitude -->
  <text class="spec" x="527" y="471" textLength="44" lengthAdjust="spacing">ALTITUDE</text>
  <text class="spec" x="527" y="484" textLength="44" lengthAdjust="spacing">60–1200</text>
  <text class="spec" x="533" y="496" textLength="32" lengthAdjust="spacing">M.N.M.</text>

  <!-- processing -->
  <text class="spec" x="599" y="471" textLength="58" lengthAdjust="spacing">PROCESSING</text>
  <line class="rule" x1="621" y1="479" x2="635" y2="479"/>
  <text class="spec" x="603" y="496" textLength="49" lengthAdjust="spacing">UNWASHED</text>

  <!-- roast marks -->
  <g class="roast-marks">
    <ellipse class="bean" cx="556" cy="530" rx="7.8" ry="9"/>
    <path class="bean-crease" d="M555 522 C552 527 559 531 556 538"/>
    <ellipse class="bean" cx="590" cy="530" rx="7.8" ry="9"/>
    <path class="bean-crease" d="M589 522 C586 527 593 531 590 538"/>
    <ellipse class="bean" cx="623" cy="530" rx="7.8" ry="9"/>
    <path class="bean-crease" d="M622 522 C619 527 626 531 623 538"/>
  </g>
</svg>
</body>
</html>
```